Bramble Hollow is company name.Handknit&crochet blankets&scarves. Need logo&business ...

I need a design that is eye catching, using yarn and is flowing. I'd like to see colors in aqua (Halvorsen Pike paint HP4817 Merilune) for the yarn and company name. For the text, a dark grey color (Halvorsen Pike HP5308 Velden Ash)

Colors
87cfc7

```html
<!DOCTYPE html>
<html lang="en">
<head>
<meta charset="utf-8">
<title>Bramble Hollow — Business Card</title>
<link rel="stylesheet" href="https://fonts.googleapis.com/css2?family=Nunito:wght@400;600;700&display=swap">
<style>
  :root {
    --aqua: #87cfc7;
    --aqua-deep: #74c6b6;
    --ash: #5f6163;
    --ash-dark: #4a4c4e;
    --paper: #ffffff;
    --backdrop: #8f8f8f;
  }
  * { box-sizing: border-box; margin: 0; padding: 0; }
  html, body {
    width: 1200px;
    height: 800px;
    overflow: hidden;
  }
  body {
    background: var(--backdrop);
    font-family: "Nunito", sans-serif;
    position: relative;
  }
  .card {
    position: absolute;
    top: 280px;
    width: 420px;
    height: 240px;
  }
  .card--front {
    left: 150px;
    background: var(--aqua-deep);
    display: flex;
    flex-direction: column;
    align-items: center;
  }
  .card--back {
    left: 630px;
    background: var(--paper);
  }
  .brand {
    display: flex;
    align-items: center;
    gap: 10px;
    font-weight: 600;
    line-height: 1.05;
  }
  .brand__dot {
    flex: none;
    border-radius: 50%;
  }
  .brand__name {
    display: flex;
    flex-direction: column;
  }
  .brand__line--second { padding-left: 0.6em; }
  .card--front .brand {
    margin-top: 52px;
    font-size: 36px;
    color: var(--paper);
  }
  .card--front .brand__dot {
    width: 12px;
    height: 12px;
    background: var(--paper);
  }
  .tagline {
    margin-top: 26px;
    text-align: center;
    color: var(--ash);
    font-size: 11px;
    font-weight: 600;
    line-height: 1.35;
  }
  .card--back .brand {
    position: absolute;
    left: 24px;
    top: 72px;
    width: 166px;
    font-size: 28px;
    color: var(--aqua);
  }
  .card--back .brand__dot {
    width: 10px;
    height: 10px;
    background: var(--aqua);
  }
  .divider {
    position: absolute;
    left: 204px;
    top: 46px;
    width: 3px;
    height: 142px;
    background: var(--aqua);
  }
  .person {
    position: absolute;
    left: 226px;
    top: 46px;
    text-align: right;
    width: 160px;
  }
  .person__name {
    font-size: 17px;
    font-weight: 700;
    color: var(--ash);
    letter-spacing: 0.2px;
  }
  .person__role {
    font-size: 10px;
    font-weight: 700;
    color: var(--ash);
  }
  .contact {
    position: absolute;
    left: 226px;
    top: 162px;
    list-style: none;
  }
  .contact__item {
    display: flex;
    align-items: center;
    gap: 8px;
    font-size: 10px;
    color: var(--ash-dark);
    height: 15px;
  }
  .contact__icon {
    width: 11px;
    height: 11px;
    flex: none;
  }
  .band {
    position: absolute;
    left: 0;
    bottom: 0;
    width: 100%;
    height: 10px;
    background: var(--aqua);
  }
</style>
</head>
<body>
  <section class="card card--front" aria-label="Card front">
    <div class="brand">
      <span class="brand__dot"></span>
      <span class="brand__name">
        <span class="brand__line">Bramble</span>
        <span class="brand__line brand__line--second">Hollow</span>
      </span>
    </div>
    <p class="tagline">
      Hand Knit<br>
      Crochet | Baby Afghans | Afghans | Scarves | Gloves | Hats
    </p>
  </section>

  <section class="card card--back" aria-label="Card back">
    <div class="brand">
      <span class="brand__dot"></span>
      <span class="brand__name">
        <span class="brand__line">Bramble</span>
        <span class="brand__line brand__line--second">Hollow</span>
      </span>
    </div>
    <div class="divider"></div>
    <div class="person">
      <p class="person__name">TESSA MARLOWE</p>
      <p class="person__role">OWNER</p>
    </div>
    <ul class="contact">
      <li class="contact__item">
        <svg class="contact__icon" viewBox="0 0 12 12" aria-hidden="true">
          <rect width="12" height="12" rx="2" fill="#87cfc7"/>
          <path d="M3.5 2.8c.4-.3.9-.2 1.1.2l.5 1c.2.3.1.7-.2.9l-.4.3c.4.9 1 1.5 1.9 1.9l.3-.4c.2-.3.6-.4.9-.2l1 .5c.4.2.5.7.2 1.1l-.4.5c-.4.4-1 .5-1.5.3C5.2 8.2 3.8 6.8 3.1 5.1c-.2-.5-.1-1.1.3-1.5z" fill="#ffffff"/>
        </svg>
        <span>xxxxxxxxxxxxxx</span>
      </li>
      <li class="contact__item">
        <svg class="contact__icon" viewBox="0 0 12 12" aria-hidden="true">
          <rect width="12" height="12" rx="2" fill="#87cfc7"/>
          <rect x="2.5" y="3.5" width="7" height="5" fill="none" stroke="#ffffff" stroke-width="1"/>
          <path d="M2.5 3.5L6 6.3l3.5-2.8" fill="none" stroke="#ffffff" stroke-width="1"/>
        </svg>
        <span>xxxxxxxxxxxxxx</span>
      </li>
    </ul>
    <div class="band"></div>
  </section>
</body>
</html>
```